Letter design, envelope design, and more

Hello, we the Vortel Gmbh are looking for our shop. Letter C5. Design does not have to be like a business card, so it can have straight lines. Only the color is important. The logo is the text under VorTel omit.It should not be playful but Profesionel

Font styles to use
Sans Serif

Colors
0555a3
3176b5
85abd2
85cae6
34a7d8
0792cd
cee9f5
cfdfed
000000

Requirements
Must have
• Color like business card, Please, with the text under VorTel, Correct address Rimbachstr. 4 Zip code 9517 Goldach, as well as Couvert Without addressing only design and logo with VorTal
Nice to have
• more writing articles
Should not have
• Not too colored, Text under VorTel, bright colors

```html
<!DOCTYPE html>
<html lang="de">
<head>
<meta charset="utf-8">
<title>VorTel Gmbh – Briefpapier</title>
<link rel="stylesheet" href="https://fonts.googleapis.com/css2?family=Open+Sans:wght@400;700&display=swap">
<style>
  :root {
    --navy: #1b2a5c;
    --brand-blue: #1277be;
    --sky-blue: #2aa3dc;
    --text-grey: #3a3a3a;
    --divider: #555a63;
    --paper: #ffffff;
    --backdrop: #ececec;
  }
  * { margin: 0; padding: 0; box-sizing: border-box; }
  html, body { width: 1200px; height: 598px; overflow: hidden; background: var(--backdrop); }
  body { font-family: "Open Sans", Arial, sans-serif; position: relative; }

  .letterhead {
    position: absolute; left: 0; top: 0;
    width: 462px; height: 598px;
    background: var(--paper);
  }
  .letterhead__top-band {
    position: absolute; left: 0; top: 0; width: 100%; height: 20px;
    background: var(--brand-blue);
  }
  .letterhead__bottom-band {
    position: absolute; left: 0; bottom: 0; width: 100%; height: 7px;
    background: var(--sky-blue);
  }

  .brand {
    position: absolute; left: 0; top: 34px; width: 100%;
    display: flex; justify-content: center; align-items: center; gap: 10px;
  }
  .brand__mark {
    width: 40px; height: 40px; background: var(--navy);
  }
  .brand__name {
    font-size: 26px; font-weight: 700; color: var(--navy);
    line-height: 1; letter-spacing: 0.5px; white-space: nowrap;
  }

  .contact-bar {
    position: absolute; left: 0; top: 521px; width: 100%; height: 40px;
  }
  .contact-item {
    position: absolute; top: 0; width: 112px; margin-left: -56px;
    text-align: center;
  }
  .contact-item svg { display: block; margin: 7px auto 4px; }
  .contact-item__text {
    font-size: 7.6px; color: var(--text-grey); letter-spacing: 1px;
    line-height: 1.15; white-space: nowrap;
  }
  .contact-item--phone .contact-item__text { letter-spacing: 0.2px; }
  .contact-item--mail .contact-item__text { letter-spacing: 0.8px; }
  .contact-divider {
    position: absolute; top: 0; width: 1px; height: 40px; background: var(--divider);
  }
</style>
</head>
<body>
  <main class="letterhead">
    <div class="letterhead__top-band"></div>

    <header class="brand">
      <div class="brand__mark"></div>
      <span class="brand__name">VorTel Gmbh</span>
    </header>

    <footer class="contact-bar">
      <div class="contact-item contact-item--phone" style="left:67px">
        <svg width="10" height="11" viewBox="0 0 10 11" aria-hidden="true">
          <rect x="2" y="0.5" width="6" height="10" rx="1.2" fill="var(--sky-blue)"/>
          <rect x="3.2" y="2" width="3.6" height="5.5" fill="#fff"/>
        </svg>
        <p class="contact-item__text">+61 000 318504</p>
      </div>
      <div class="contact-divider" style="left:106px"></div>

      <div class="contact-item" style="left:165px">
        <svg width="12" height="11" viewBox="0 0 12 11" aria-hidden="true">
          <path d="M6 0.5 L11.5 5.5 H10 V10.5 H7.3 V7.3 H4.7 V10.5 H2 V5.5 H0.5 Z" fill="var(--sky-blue)"/>
        </svg>
        <p class="contact-item__text">Rimbachstr. 4<br>9517 Goldach</p>
      </div>
      <div class="contact-divider" style="left:223px"></div>

      <div class="contact-item" style="left:286px">
        <svg width="11" height="11" viewBox="0 0 12 12" aria-hidden="true">
          <circle cx="6" cy="6" r="5.5" fill="var(--sky-blue)"/>
          <g fill="none" stroke="#fff" stroke-width="0.7">
            <ellipse cx="6" cy="6" rx="2.3" ry="5.5"/>
            <line x1="0.5" y1="6" x2="11.5" y2="6"/>
            <line x1="1.5" y1="3.3" x2="10.5" y2="3.3"/>
            <line x1="1.5" y1="8.7" x2="10.5" y2="8.7"/>
          </g>
        </svg>
        <p class="contact-item__text">www.vortel-web.com</p>
      </div>
      <div class="contact-divider" style="left:341px"></div>

      <div class="contact-item contact-item--mail" style="left:400px">
        <svg width="11" height="9" viewBox="0 0 11 8" aria-hidden="true">
          <rect x="0" y="0" width="11" height="8" fill="var(--sky-blue)"/>
          <path d="M0.5 0.7 L5.5 4.5 L10.5 0.7" fill="none" stroke="#fff" stroke-width="0.8"/>
        </svg>
        <p class="contact-item__text">info@vortel-mail.com</p>
      </div>
    </footer>

    <div class="letterhead__bottom-band"></div>
  </main>
</body>
</html>
```